BCR 2014 Seasons Greetings

Christmas postcards.
Side A: Image with 3 logos "Vareno Cove Lodge" "Kilimu Lodge Samoa" "Sefa Lani"(Logos on bottom of card" & "Seasons Greetings" (to fit)
Side B Left:
Text
"Management and staff at Orrinvale Lodges wish you and your family a very happy and safe festive season and all the best for the New Year.
Counting down your next arrival"
Side B Right: Address template with 4 lines & Area for stamp top right corner.
Side B Base: Logo & Website "Orrinvale Lodges" " www.orrinvalelodges.example"
High end travel
Management

```html
<!DOCTYPE html>
<html lang="en">
<head>
<meta charset="utf-8">
<title>Orrinvale Lodges – Season's Greetings Postcard</title>
<link rel="stylesheet" href="https://fonts.googleapis.com/css2?family=Poiret+One&family=Montserrat:wght@400&family=Mukta:wght@400&family=Arimo:wght@400&display=swap">
<style>
  :root {
    --stage: #4d4d4d;
    --card: #ffffff;
    --ink: #2b2b2b;
    --ink-soft: #555555;
    --rule: #8a8a8a;
    --white: #ffffff;
    --sea-deep: #0f4a6b;
    --sea-mid: #2f7ea3;
    --sea-light: #a9d3e6;
    --sky: #e3f0f6;
  }
  * { margin: 0; padding: 0; box-sizing: border-box; }
  html, body {
    width: 1000px; height: 1200px; overflow: hidden;
    background: var(--stage);
  }
  .postcard {
    position: absolute; left: 131px; width: 728px; height: 564px;
    background: var(--card);
    box-shadow: 0 1px 2px rgba(0,0,0,.35);
    overflow: hidden;
  }
  .postcard--front { top: 25px; }
  .postcard--back { top: 614px; }

  /* Front */
  .front__photo {
    position: absolute; inset: 0;
    background:
      radial-gradient(ellipse 38% 22% at 52% 34%, var(--sky) 0%, rgba(227,240,246,.6) 45%, rgba(227,240,246,0) 100%),
      radial-gradient(ellipse 30% 45% at 88% 25%, rgba(200,228,240,.85) 0%, rgba(200,228,240,0) 100%),
      radial-gradient(ellipse 55% 50% at 55% 70%, var(--sea-mid) 0%, rgba(47,126,163,0) 100%),
      linear-gradient(100deg, var(--sea-deep) 0%, #1f6688 35%, #3f8fb4 65%, #5d9fc0 100%);
  }
  .front__title {
    position: absolute; left: 56px; top: 70px;
    font-family: "Poiret One", sans-serif; font-weight: 400;
    font-size: 56px; line-height: 1; color: var(--ink);
    letter-spacing: 0;
    white-space: nowrap;
  }
  .front__lodges {
    position: absolute; left: 57px; top: 470px;
    display: flex; flex-direction: column; gap: 3px;
    list-style: none;
    color: var(--white);
    font-family: "Arimo", sans-serif; font-size: 10px;
  }
  .lodge-name { display: flex; align-items: center; gap: 5px; }
  .lodge-name::before {
    content: ""; width: 8px; height: 8px; border-radius: 50%;
    border: 1.5px solid var(--white);
  }
  .front__url {
    position: absolute; left: 57px; top: 510px;
    font-family: "Arimo", sans-serif; font-size: 13px; color: var(--white);
  }
  .brand {
    display: flex; align-items: center;
    font-family: "Montserrat", sans-serif; font-weight: 400;
    text-transform: uppercase; letter-spacing: 2px; white-space: nowrap;
  }
  .brand__dot { border-radius: 50%; flex: none; }
  .front__brand {
    position: absolute; left: 358px; top: 502px;
    color: var(--white); font-size: 13px; gap: 14px;
  }
  .front__brand .brand__dot { width: 22px; height: 22px; background: var(--white); }

  /* Back */
  .back__brand {
    position: absolute; left: 33px; top: 64px;
    color: var(--ink-soft); font-size: 11px; gap: 56px;
  }
  .back__brand .brand__dot { width: 22px; height: 22px; background: var(--ink-soft); }
  .back__divider {
    position: absolute; left: 352px; top: 37px; width: 1px; height: 485px;
    background: var(--rule);
  }
  .back__message {
    position: absolute; left: 52px; top: 196px; width: 276px;
    font-family: "Mukta", sans-serif; font-size: 15.5px; line-height: 20.5px;
    color: var(--ink-soft);
  }
  .back__message p { text-align: justify; }
  .back__message p + p { margin-top: 20.5px; text-align: left; }
  .back__website {
    position: absolute; left: 51px; top: 431px; width: 282px;
    font-family: "Mukta", sans-serif; font-size: 21px; line-height: 1.2;
    color: var(--ink-soft); white-space: nowrap;
  }
  .address-lines { position: absolute; left: 0; top: 0; }
</style>
</head>
<body>
  <section class="postcard postcard--front" aria-label="Postcard front">
    <div class="front__photo" role="img" aria-label="Photograph from inside a curling blue ocean wave, looking out to a green island and a small boat on calm water"></div>
    <h1 class="front__title">Season’s Greetings!</h1>
    <ul class="front__lodges">
      <li class="lodge-name">Vareno Cove Lodge</li>
      <li class="lodge-name">Kilimu Lodge Samoa</li>
      <li class="lodge-name">Sefa Lani</li>
    </ul>
    <div class="front__url">varenocovelodge.example</div>
    <div class="brand front__brand"><span class="brand__dot"></span><span>Orrinvale Lodges &amp; Resorts</span></div>
  </section>

  <section class="postcard postcard--back" aria-label="Postcard back">
    <div class="brand back__brand"><span class="brand__dot"></span><span>Orrinvale Lodges &amp; Resorts</span></div>
    <div class="back__message">
      <p>Management and staff at Orrinvale Lodges wish you and your family a very happy and safe festive season and all the best for the New Year.</p>
      <p>We look forward to seeing you soon!</p>
    </div>
    <div class="back__website">www.orrinvalelodges.example</div>
    <div class="back__divider"></div>
    <svg class="address-lines" width="728" height="564" viewBox="0 0 728 564" aria-hidden="true">
      <g stroke="#8a8a8a" stroke-width="1">
        <line x1="385" y1="233.5" x2="657" y2="233.5"/>
        <line x1="387" y1="296.5" x2="660" y2="296.5"/>
        <line x1="387" y1="351.5" x2="660" y2="351.5"/>
        <line x1="387" y1="407.5" x2="660" y2="407.5"/>
      </g>
    </svg>
  </section>
</body>
</html>
```